Ladles and Lanterns App design

I need a full app design, colours, images, fonts, and a mock up design of the app to bring to the developer.

Ladles and Lanterns is a free app that allows cafes, independent cafe and chains of cafes to let their customers know what the soup of the day and what specials they have on that day through the app. Each cafe will have a profile which they can upload the Ladles and Lanterns daily.

The user home screen will include google maps showing their location with the registered cafes and eateries around them. including a list of the cafe and distances below. as seen in attachment.

Target Market(s)

Cafes , anyone who enjoys eating soups and off local cafe specials boards

Requirements
Must have
• I would like a complete app design based on the attached images.

```html
<!DOCTYPE html>
<html lang="en">
<head>
<meta charset="utf-8">
<title>Ladles and Lanterns – Home</title>
<link rel="stylesheet" href="https://fonts.googleapis.com/css2?family=Roboto:wght@700&family=Nunito:wght@800&family=Quicksand:wght@400;500&display=swap">
<style>
  :root {
    --brand-red: #e85756;
    --brand-red-soft: #f8b9b6;
    --panel-brown: #7b5b58;
    --ink: #3b3b3b;
    --ink-soft: #6b6b6b;
    --rule: #d9d9d9;
    --surface: #ffffff;
    --map-base: #efefef;
    --map-block: #e6e6e6;
    --map-peach: #fbe9d9;
    --map-park: #c5e8b4;
    --map-road: #f7df86;
  }
  * { box-sizing: border-box; margin: 0; padding: 0; }
  html, body { width: 1200px; height: 2598px; overflow: hidden; background: var(--surface); }
  .screen { position: relative; width: 1200px; height: 2598px; overflow: hidden; background: var(--surface); font-family: "Quicksand", sans-serif; }

  .map-area {
    position: absolute; left: 0; top: 0; width: 1200px; height: 1742px;
    background:
      radial-gradient(ellipse 170px 150px at 760px 1010px, var(--map-park) 0%, rgba(197,232,180,0.6) 55%, rgba(197,232,180,0) 100%),
      radial-gradient(ellipse 220px 140px at 1120px 400px, var(--map-road) 0%, rgba(247,223,134,0) 100%),
      radial-gradient(ellipse 360px 520px at 140px 950px, var(--map-peach) 0%, rgba(251,233,217,0.7) 50%, rgba(251,233,217,0) 100%),
      radial-gradient(ellipse 300px 260px at 330px 1450px, var(--map-peach) 0%, rgba(251,233,217,0) 100%),
      radial-gradient(ellipse 260px 200px at 420px 700px, rgba(251,233,217,0.8) 0%, rgba(251,233,217,0) 100%),
      linear-gradient(160deg, var(--map-base) 0%, var(--map-block) 60%, var(--map-base) 100%);
  }

  .app-header {
    position: absolute; left: 0; top: 0; width: 1200px; height: 355px;
    background: var(--brand-red); border-radius: 0 0 110px 110px;
  }
  .status-bar { position: absolute; left: 0; top: 0; width: 100%; height: 140px; color: #fff; }
  .status-time { position: absolute; left: 104px; top: 44px; font: 700 48px "Roboto", sans-serif; }
  .status-icons { position: absolute; right: 48px; top: 52px; }
  .app-title {
    position: absolute; left: 0; right: 0; top: 199px; text-align: center;
    color: #fff; font: 700 82px/96px "Roboto", sans-serif; letter-spacing: 0.5px;
  }

  .search-bar {
    position: absolute; left: 90px; top: 406px; width: 1030px; height: 150px;
    background: var(--surface); border-radius: 75px;
    box-shadow: 0 6px 20px rgba(0,0,0,0.12);
  }
  .search-icon { position: absolute; left: 78px; top: 50px; }
  .search-placeholder { position: absolute; left: 175px; top: 50px; font: 500 42px "Quicksand", sans-serif; color: var(--ink-soft); }
  .filter-icon { position: absolute; right: 75px; top: 46px; }

  .price-tag {
    position: absolute; height: 110px; border-radius: 55px;
    background: var(--brand-red); border: 5px solid #fff;
    color: #fff; font: 800 34px "Nunito", sans-serif;
    display: flex; align-items: center; justify-content: center;
    box-shadow: 0 4px 14px rgba(0,0,0,0.15);
  }
  .price-tag--mushroom { left: 628px; top: 776px; width: 526px; }
  .price-tag--tomato { left: 332px; top: 1196px; width: 460px; }

  .nearest-panel {
    position: absolute; left: 75px; top: 1586px; width: 1062px; height: 686px;
    background: var(--surface); border-radius: 75px; overflow: hidden;
    box-shadow: 0 8px 26px rgba(0,0,0,0.14);
  }
  .nearest-panel__header {
    height: 120px; background: var(--panel-brown); color: #fff;
    display: flex; align-items: center; padding-left: 95px; gap: 28px;
    font: 500 44px "Quicksand", sans-serif;
  }
  .establishment-list { list-style: none; margin: 0 72px; }
  .establishment-row {
    position: relative; height: 122px; border-bottom: 2px solid var(--rule);
    font: 400 40px "Quicksand", sans-serif; color: var(--ink);
  }
  .establishment-row:first-child { height: 145px; }
  .establishment-row span { position: absolute; bottom: 38px; }
  .col-name { left: 22px; }
  .col-soup { left: 330px; width: 0; display: flex; justify-content: center; white-space: nowrap; }
  .col-special { left: 522px; }
  .col-distance { right: 32px; }

  .tab-bar {
    position: absolute; left: 0; top: 2376px; width: 1200px; height: 222px;
    background: var(--brand-red); border-radius: 110px 110px 0 0;
  }
  .tab-pill {
    position: absolute; left: 75px; top: 59px; width: 295px; height: 113px;
    background: var(--surface); border-radius: 57px;
    display: flex; align-items: center; justify-content: center; gap: 16px;
    color: var(--brand-red); font: 800 44px "Nunito", sans-serif;
  }
  .tab-icon { position: absolute; top: 82px; }
</style>
</head>
<body>
<main class="screen">
  <div class="map-area" role="img" aria-label="Street map of the user's surroundings with streets, a park and nearby cafes and eateries"></div>

  <header class="app-header">
    <div class="status-bar">
      <span class="status-time">9:41</span>
      <svg class="status-icons" width="210" height="40" viewBox="0 0 210 40" fill="#fff">
        <rect x="0" y="26" width="9" height="12" rx="2"/><rect x="14" y="19" width="9" height="19" rx="2"/>
        <rect x="28" y="11" width="9" height="27" rx="2"/><rect x="42" y="3" width="9" height="35" rx="2"/>
        <path d="M85 36 l-7-8 a11 11 0 0 1 14 0z"/>
        <path d="M70 19 a22 22 0 0 1 30 0 l-4 5 a15 15 0 0 0 -22 0z"/>
        <path d="M62 10 a34 34 0 0 1 46 0 l-4 5 a27 27 0 0 0 -38 0z"/>
        <rect x="132" y="4" width="70" height="32" rx="9" fill="none" stroke="#fff" stroke-width="3" opacity="0.6"/>
        <rect x="137" y="9" width="60" height="22" rx="5"/>
      </svg>
    </div>
    <h1 class="app-title">Ladles and Lanterns</h1>
  </header>

  <div class="search-bar">
    <svg class="search-icon" width="52" height="52" viewBox="0 0 52 52" fill="none" stroke="#e85756" stroke-width="5" stroke-linecap="round">
      <circle cx="22" cy="22" r="17"/><line x1="35" y1="35" x2="48" y2="48"/>
    </svg>
    <span class="search-placeholder">Seach Soups</span>
    <svg class="filter-icon" width="58" height="58" viewBox="0 0 58 58" fill="none" stroke="#e85756" stroke-width="3.5">
      <rect x="2" y="2" width="54" height="54" rx="10"/>
      <line x1="10" y1="17" x2="48" y2="17"/><line x1="10" y1="29" x2="48" y2="29"/><line x1="10" y1="41" x2="48" y2="41"/>
      <circle cx="37" cy="17" r="4" fill="#fff"/><circle cx="20" cy="29" r="4" fill="#fff"/><circle cx="33" cy="41" r="4" fill="#fff"/>
    </svg>
  </div>

  <div class="price-tag price-tag--mushroom">$500 - Murshroom Special</div>
  <div class="price-tag price-tag--tomato">$300 - Tomato Special</div>

  <section class="nearest-panel">
    <h2 class="nearest-panel__header">
      <svg width="54" height="48" viewBox="0 0 54 48" fill="#fff">
        <path d="M14 2 q-4 4 0 8 q4 4 0 8" stroke="#fff" stroke-width="3" fill="none"/>
        <path d="M25 2 q-4 4 0 8 q4 4 0 8" stroke="#fff" stroke-width="3" fill="none"/>
        <path d="M36 2 q-4 4 0 8 q4 4 0 8" stroke="#fff" stroke-width="3" fill="none"/>
        <rect x="0" y="24" width="54" height="5" rx="2"/>
        <path d="M3 31 h48 q-4 12 -16 12 h-16 q-12 0 -16 -12z"/>
        <rect x="14" y="44" width="26" height="4" rx="2"/>
      </svg>
      <span>Nearest Establishments</span>
    </h2>
    <ul class="establishment-list">
      <li class="establishment-row"><span class="col-name">Name</span><span class="col-soup">Tomato</span><span class="col-special">Special</span><span class="col-distance">800m</span></li>
      <li class="establishment-row"><span class="col-name">Name</span><span class="col-soup">Mushroom</span><span class="col-special">Special</span><span class="col-distance">300m</span></li>
      <li class="establishment-row"><span class="col-name">Name</span><span class="col-soup">Sweet Corn</span><span class="col-special">Special</span><span class="col-distance">500m</span></li>
      <li class="establishment-row"><span class="col-name">Name</span><span class="col-soup">Sweet Corn</span><span class="col-special">Special</span><span class="col-distance">500m</span></li>
    </ul>
  </section>

  <nav class="tab-bar">
    <div class="tab-pill">
      <svg width="70" height="62" viewBox="0 0 54 48" fill="#e85756">
        <path d="M14 2 q-4 4 0 8 q4 4 0 8" stroke="#e85756" stroke-width="3" fill="none"/>
        <path d="M25 2 q-4 4 0 8 q4 4 0 8" stroke="#e85756" stroke-width="3" fill="none"/>
        <path d="M36 2 q-4 4 0 8 q4 4 0 8" stroke="#e85756" stroke-width="3" fill="none"/>
        <rect x="0" y="24" width="54" height="5" rx="2"/>
        <path d="M3 31 h48 q-4 12 -16 12 h-16 q-12 0 -16 -12z"/>
        <rect x="14" y="44" width="26" height="4" rx="2"/>
      </svg>
      <span>Soups</span>
    </div>
    <svg class="tab-icon" style="left:474px" width="66" height="66" viewBox="0 0 66 66" fill="#f8b9b6">
      <path d="M20 2 q-5 5 0 10 q5 5 0 10" stroke="#f8b9b6" stroke-width="4" fill="none"/>
      <path d="M33 2 q-5 5 0 10 q5 5 0 10" stroke="#f8b9b6" stroke-width="4" fill="none"/>
      <path d="M46 2 q-5 5 0 10 q5 5 0 10" stroke="#f8b9b6" stroke-width="4" fill="none"/>
      <rect x="2" y="28" width="62" height="7" rx="3"/>
      <path d="M5 38 h56 q-4 20 -22 20 h-12 q-18 0 -22 -20z"/>
      <path d="M10 44 q6 -4 12 0 t12 0 t12 0 t12 0" stroke="#e85756" stroke-width="3" fill="none"/>
    </svg>
    <svg class="tab-icon" style="left:764px" width="60" height="70" viewBox="0 0 60 70" fill="#f8b9b6">
      <circle cx="30" cy="17" r="16"/><path d="M2 70 v-12 q0 -20 28 -20 q28 0 28 20 v12z"/>
    </svg>
    <svg class="tab-icon" style="left:1046px" width="68" height="68" viewBox="0 0 68 68">
      <path fill="#f8b9b6" d="M29 2h10l2 9 6 3 8-5 7 7-5 8 3 6 9 2v10l-9 2-3 6 5 8-7 7-8-5-6 3-2 9H29l-2-9-6-3-8 5-7-7 5-8-3-6-9-2V29l9-2 3-6-5-8 7-7 8 5 6-3z"/>
      <circle cx="34" cy="34" r="13" fill="none" stroke="#e85756" stroke-width="4"/>
      <circle cx="34" cy="34" r="6" fill="#e85756"/>
    </svg>
  </nav>
</main>
</body>
</html>
```